"Broadcast Tinkerings" - podcast cover artwrok

I need podcast cover artwork for "Broadcast Tinkerings". As the name implies, it focuses on experimenting with podcasts. I started this podcast a couple years ago and am rebranding now (old name was "Lantern Workshop" with the tagline of "broadcast tinkerings).

Maybe have (in small type) "a production of Harbor Fern Audio, LLC".

I would like it to convey creativity, innovation, and simplicity.

UPDATE: I uploaded a couple other podcast artwork I like to help with inspiration.

Target Market(s)

Podcasters, bloggers, entrepreneurs

Font styles to use
Sans Serif

Colors
0355a3
acd036
faa54b

Requirements
Must have
• Colors I like are darker shades of blue, green, and tan/sand. I selected sample colors, but the shade can vary to ensure that they are complementary.
Nice to have
• I've included a cartoon image of myself that may or may not work with the design.

```html
<!DOCTYPE html>
<html lang="en">
<head>
<meta charset="utf-8">
<title>Broadcast Tinkerings — Podcast Cover</title>
<link href="https://fonts.googleapis.com/css2?family=Lilita+One&family=Oswald:wght@600&display=swap" rel="stylesheet">
<style>
  :root {
    --page: #ffffff;
    --card-top: #f4f4f4;
    --card-bottom: #dcdcdc;
    --title-orange: #f7941d;
    --title-edge: #3a3a3a;
    --ink-dark: #2b2b2b;
    --brand-red: #c0272d;
    --blue: #0355a3;
    --blue-light: #1a86cf;
    --teal: #1f7fa8;
    --red: #b8202a;
    --yellow: #e9b520;
    --green: #6e9a1f;
    --green-light: #acd036;
    --grey: #8d8f93;
    --white: #ffffff;
  }
  * { box-sizing: border-box; margin: 0; padding: 0; }
  html, body { width: 1200px; height: 1106px; overflow: hidden; background: var(--page); }
  .cover {
    position: relative;
    width: 1200px;
    height: 1106px;
    overflow: hidden;
    background: var(--page);
  }
  .cover-card {
    position: absolute;
    left: 37px; top: 22px;
    width: 1148px; height: 1030px;
    background: linear-gradient(160deg, var(--card-top) 0%, #ececec 45%, var(--card-bottom) 100%);
    box-shadow: 6px 8px 14px rgba(0,0,0,0.35);
    overflow: hidden;
  }
  .swooshes { position: absolute; inset: 0; width: 100%; height: 100%; }
  .show-title {
    position: absolute;
    left: 56px; top: 54px;
    font-family: "Lilita One", "Arial Black", sans-serif;
    font-size: 112px;
    line-height: 1.02;
    letter-spacing: 3px;
    color: var(--title-orange);
    -webkit-text-stroke: 3px var(--title-edge);
    text-shadow: 5px 6px 0 rgba(60,60,60,0.55);
  }
  .show-title span { display: block; }
  .network-mark {
    position: absolute;
    left: 900px; top: 30px;
    width: 220px;
    display: flex;
    flex-direction: column;
    align-items: center;
    gap: 10px;
    font-family: "Lilita One", "Arial Black", sans-serif;
    font-size: 34px;
    line-height: 1.05;
    text-align: center;
    color: var(--ink-dark);
  }
  .network-mark .dot {
    width: 46px; height: 46px;
    border-radius: 50%;
    background: var(--ink-dark);
  }
  .host-portrait {
    position: absolute;
    left: 180px; top: 290px;
    width: 530px; height: 396px;
    border-radius: 50%;
    background: radial-gradient(ellipse at 45% 45%, #f3d2bd 0%, #d8e9f0 55%, #ffffff 80%);
    box-shadow: -4px 6px 10px rgba(0,0,0,0.3);
  }
  .pointer { position: absolute; left: 655px; top: 495px; width: 58px; height: 62px; }
  .cta {
    position: absolute;
    left: 606px; top: 522px;
    width: 380px; height: 270px;
    border-radius: 50%;
    background: var(--white);
    box-shadow: 0 4px 10px rgba(0,0,0,0.3);
    display: flex; align-items: center; justify-content: center;
  }
  .cta-button {
    width: 308px; height: 178px;
    border-radius: 50%;
    background: radial-gradient(ellipse at 40% 30%, var(--blue-light) 0%, var(--blue) 70%, #023e78 100%);
    display: flex; align-items: center; justify-content: center;
    font-family: "Oswald", "Arial Narrow", sans-serif;
    font-weight: 600;
    font-size: 52px;
    color: var(--white);
    transform: rotate(4deg);
    letter-spacing: 1px;
  }
</style>
</head>
<body>
<div class="cover">
  <div class="cover-card">
    <svg class="swooshes" viewBox="0 0 1148 1030" preserveAspectRatio="none">
      <defs>
        <linearGradient id="blueBand" x1="0" y1="0" x2="1" y2="1">
          <stop offset="0" stop-color="#1f9bd6"/>
          <stop offset="1" stop-color="#034a8c"/>
        </linearGradient>
        <linearGradient id="greenBars" x1="0" y1="0" x2="1" y2="1">
          <stop offset="0" stop-color="#8cb62a"/>
          <stop offset="1" stop-color="#4f7a14"/>
        </linearGradient>
      </defs>
      <path role="img" aria-label="Green stepped bar graphic" d="M620 520 L1148 300 L1148 1030 L820 1030 Z" fill="url(#greenBars)" opacity="0.85"/>
      <path d="M0 230 C120 420 260 560 500 620 C700 670 900 680 1148 690 L1148 740 C880 740 640 730 440 680 C220 620 80 470 0 330 Z" fill="url(#blueBand)"/>
      <path d="M0 600 C200 690 420 730 700 760 C900 780 1040 800 1148 820 L1148 860 C960 840 760 820 520 800 C300 780 130 730 0 690 Z" fill="var(--red)"/>
      <path d="M0 690 C220 760 460 800 720 830 C900 850 1040 880 1148 910 L1148 950 C980 915 800 890 560 870 C320 850 140 800 0 760 Z" fill="var(--yellow)"/>
      <path d="M0 760 C240 840 520 880 800 905 C960 920 1060 940 1148 960 L1148 1000 C980 975 780 960 520 940 C300 920 120 870 0 830 Z" fill="var(--teal)"/>
      <path d="M0 830 C260 910 560 950 840 970 C980 980 1080 995 1148 1010 L1148 1030 L0 1030 Z" fill="var(--grey)"/>
      <path d="M0 900 C300 960 620 990 1148 1030 L0 1030 Z" fill="#5b3b6e" opacity="0.55"/>
    </svg>

    <h1 class="show-title"><span>BROADCAST</span><span>TINKERINGS</span></h1>

    <div class="network-mark">
      <span class="dot"></span>
      <span>The Signal Ledger</span>
    </div>

    <div class="host-portrait" role="img" aria-label="Cartoon portrait of the show host"></div>

    <svg class="pointer" viewBox="0 0 58 62" aria-hidden="true">
      <path d="M4 4 L4 50 L16 39 L25 58 L33 54 L24 36 L40 36 Z" fill="#ffffff" stroke="#1a86cf" stroke-width="3" stroke-linejoin="round"/>
    </svg>

    <div class="cta"><div class="cta-button">STARET NOW</div></div>
  </div>
</div>
</body>
</html>
```